Navelo Partnering Business Card

Hello everyone. We need a business card design that would match our logo and the theme we're trying to have for Navelo that you can find on our website and/or Corvapage page

```html
<!DOCTYPE html>
<html lang="en">
<head>
<meta charset="utf-8">
<title>Navelo Partnering Business Card</title>
<link href="https://fonts.googleapis.com/css2?family=Lato:wght@400;700;900&display=swap" rel="stylesheet">
<style>
  :root {
    --stage: #202022;
    --navy: #1b3566;
    --purple: #3b1f60;
    --paper: #ffffff;
    --gold: #f0b92a;
    --teal: #1fb3ad;
    --ink-light: #ffffff;
  }
  * { margin: 0; padding: 0; box-sizing: border-box; }
  html, body {
    width: 1200px; height: 900px; overflow: hidden;
    background: var(--stage);
    font-family: "Lato", sans-serif;
  }
  .stage { position: relative; width: 1200px; height: 900px; }
  .card {
    position: absolute;
    width: 600px; height: 343px;
    border-radius: 16px;
    overflow: hidden;
    box-shadow: 0 14px 30px rgba(0,0,0,0.45);
  }
  .card-front { left: 150px; top: 80px; background: var(--navy); }
  .card-back { left: 450px; top: 470px; display: flex; }

  .pattern-area {
    position: absolute; left: 0; top: 70px;
    width: 600px; height: 120px;
    background: linear-gradient(180deg,
      rgba(240,185,42,0.55) 0%,
      rgba(255,255,255,0.45) 50%,
      rgba(31,179,173,0.55) 100%);
  }

  .brand {
    display: flex; align-items: center; gap: 12px;
    font-weight: 900; letter-spacing: -0.5px;
  }
  .brand-dot { border-radius: 50%; flex: none; }

  .card-front .brand {
    position: absolute; left: 40px; bottom: 52px;
    color: var(--ink-light); font-size: 54px;
  }
  .card-front .brand-dot { width: 22px; height: 22px; background: var(--ink-light); }

  .back-logo-side {
    width: 47%; background: var(--paper);
    display: flex; align-items: center; justify-content: center;
  }
  .back-logo-side .brand { color: var(--purple); font-size: 60px; }
  .back-logo-side .brand-dot { width: 24px; height: 24px; background: var(--purple); }

  .back-info-side {
    flex: 1; background: var(--purple); color: var(--ink-light);
    padding: 74px 0 0 44px;
  }
  .holder-name { font-size: 17px; font-weight: 400; letter-spacing: 0.5px; text-transform: uppercase; }
  .holder-name strong { font-weight: 700; }
  .holder-role { font-size: 14px; margin-top: 4px; padding-left: 18px; }
  .contact-list { list-style: none; margin-top: 34px; }
  .contact-list li {
    display: flex; align-items: center; gap: 12px;
    font-size: 14px; line-height: 1; margin-bottom: 11px;
  }
  .contact-icon { width: 14px; height: 14px; flex: none; }
</style>
</head>
<body>
<main class="stage">
  <section class="card card-front" aria-label="Card front">
    <div class="pattern-area" role="img" aria-label="Decorative flowing line pattern in gold, white and teal"></div>
    <div class="brand"><span class="brand-dot"></span>Navelo</div>
  </section>

  <section class="card card-back" aria-label="Card back">
    <div class="back-logo-side">
      <div class="brand"><span class="brand-dot"></span>Navelo</div>
    </div>
    <div class="back-info-side">
      <p class="holder-name">Aino <strong>Rautio</strong></p>
      <p class="holder-role">Managing Director</p>
      <ul class="contact-list">
        <li>
          <svg class="contact-icon" viewBox="0 0 16 16" aria-hidden="true"><path fill="#fff" d="M3 1h3l1.5 4-2 1.3a9 9 0 0 0 4.2 4.2L11 8.5l4 1.5v3a2 2 0 0 1-2 2A12 12 0 0 1 1 3a2 2 0 0 1 2-2z"/></svg>
          +61 02 5550 0147
        </li>
        <li>
          <svg class="contact-icon" viewBox="0 0 16 16" aria-hidden="true"><rect x="1" y="3" width="14" height="10" fill="#fff"/><path d="M1 3l7 6 7-6" fill="none" stroke="#3b1f60" stroke-width="1.4"/></svg>
          aino@navelohub.com
        </li>
        <li>
          <svg class="contact-icon" viewBox="0 0 16 16" aria-hidden="true"><circle cx="8" cy="8" r="6" fill="#fff"/></svg>
          corvapage.com/navelo
        </li>
      </ul>
    </div>
  </section>
</main>
</body>
</html>
```